Healthcare marketing Website design

This is for a healthcare marketing agency
All details and brief included in the files

I need the design to be incredible!

5 pages to be designed
Home page
About
Portfolio Page
Services
Start your project page

If you need more stock images - download preview images from kelmora pix so I can purchase at a later date

```html
<!DOCTYPE html>
<html lang="en">
<head>
<meta charset="utf-8">
<title>Meridian Reach — Healthcare Marketing</title>
<link href="https://fonts.googleapis.com/css2?family=Comfortaa:wght@400;500&family=Poppins:wght@300;400;500;600;700&display=swap" rel="stylesheet">
<style>
:root{
  --ink:#22243a;
  --text:#3a3c4e;
  --muted:#9a9cab;
  --blue:#1a9be2;
  --send:#3d63f3;
  --lav:#e6e6fb;
  --panel:#e9ebfc;
  --dark:#2d2e40;
  --footer:#262839;
  --line:#d9dae4;
  --orange:#f29a4a;
  --wave:#e7d3f7;
}
*{margin:0;padding:0;box-sizing:border-box}
html,body{width:1200px;height:4866px;overflow:hidden}
body{position:relative;font-family:'Poppins',sans-serif;color:var(--text);
  background:
   radial-gradient(ellipse 520px 420px at 1150px 750px,#e3e4fc 0%,transparent 70%),
   radial-gradient(ellipse 600px 500px at 80px 380px,#ecebfd 0%,transparent 70%),
   radial-gradient(ellipse 500px 500px at 1100px 2150px,#e4e6fc 0%,transparent 70%),
   radial-gradient(ellipse 480px 420px at 100px 2950px,#eceefd 0%,transparent 70%),
   radial-gradient(ellipse 520px 420px at 1150px 3450px,#e6e7fc 0%,transparent 70%),
   #fbfbff;}
.abs{position:absolute}
.display{font-family:'Comfortaa',sans-serif;font-weight:400;color:var(--ink)}
.brand{display:flex;align-items:center;gap:10px;font-family:'Poppins',sans-serif;font-weight:500;font-size:26px;color:var(--blue)}
.brand-dot{width:28px;height:28px;border-radius:50%;background:var(--blue)}
.nav{left:645px;top:44px;display:flex;gap:30px;font-size:14px;color:var(--text)}
.link{display:flex;align-items:center;gap:10px;font-size:16px;font-weight:600;color:var(--blue)}
.link svg{width:36px;height:36px}
.hero-band{left:0;top:380px;width:1200px;height:250px;
  background:linear-gradient(170deg,transparent 20%,rgba(231,211,247,.45) 50%,transparent 80%)}
.social{display:flex;gap:8px}
.social span{width:32px;height:32px;border-radius:50%;background:var(--ink);display:block}
.stats{left:202px;top:970px;width:805px;height:226px;border-radius:24px;background:linear-gradient(90deg,#f1f1fd,#e3e5fc)}
.stat{position:absolute;display:flex;align-items:center;gap:32px;font-size:13px;line-height:25px;color:var(--ink)}
.gem{width:60px;height:60px;border-radius:14px;background:var(--blue);transform:rotate(45deg);display:flex;align-items:center;justify-content:center;margin-left:12px}
.gem b{transform:rotate(-45deg);color:#fff;font-size:22px;font-weight:700}
.service{position:absolute;width:150px;text-align:center;font-size:16px;font-weight:600;color:var(--ink);line-height:24px}
.service svg{width:140px;height:140px;display:block;margin:0 auto 8px}
.card{position:absolute;width:158px;height:197px;border:2px solid var(--ink);border-radius:14px;background:#fff;box-shadow:0 10px 22px rgba(40,40,90,.12);text-align:center;padding-top:44px}
.card b{display:block;font-size:38px;font-weight:700;color:var(--ink)}
.card span{display:block;font-size:16px;color:var(--ink);line-height:34px;margin-top:2px}
.avatar{position:absolute;border-radius:50%;border:2px dotted #777;padding:5px}
.avatar i{display:block;width:100%;height:100%;border-radius:50%;background:linear-gradient(135deg,#b9a79a,#5a5560)}
.quote{left:372px;top:2699px;width:500px;height:265px;background:var(--dark);border-radius:4px;color:#c9cad4;text-align:center;font-size:14px;line-height:25px;padding:30px 40px;box-shadow:0 20px 40px rgba(30,30,60,.25)}
.quote .who{margin-top:32px;font-weight:600;font-size:14px;letter-spacing:.5px;color:#c9cad4}
.faq{left:232px;width:736px}
.faq-q{display:flex;justify-content:space-between;font-size:18px;color:var(--ink);height:130px;padding-top:10px;border-bottom:1px solid var(--line)}
.faq-q.open{height:210px}
.faq-a{font-size:16px;line-height:27px;color:var(--text);margin-top:18px;padding-left:6px;width:620px}
.post{position:absolute;top:3927px;width:295px}
.post .photo{height:284px;border-radius:4px}
.post .meta{margin-top:48px;font-size:11px;color:var(--text)}
.post .meta em{font-style:normal;color:var(--orange)}
.post h3{font-size:19px;font-weight:500;color:var(--ink);margin-top:6px}
.post .more{display:inline-block;margin-top:18px;font-size:14px;font-weight:600;color:var(--ink);padding-bottom:10px;border-bottom:2px solid var(--ink);width:84px}
.footer{left:0;top:4451px;width:1200px;height:415px;background:var(--footer);color:#c5c6d2}
.footer h4{font-size:16px;font-weight:600;color:#fff;margin-bottom:16px}
.footer ul{list-style:none;font-size:13px;line-height:24px}
.input{width:248px;height:46px;background:#323447;color:#a9aabb;font-size:13px;padding:13px 18px}
.send{width:92px;height:38px;background:var(--send);color:#fff;font-size:13px;text-align:center;line-height:38px;border-radius:2px;margin-top:20px}
.foot-social span{width:26px;height:26px;background:#fff}
</style>
</head>
<body>

<header>
  <div class="abs brand" style="left:132px;top:34px"><span class="brand-dot"></span>meridian reach</div>
  <nav class="abs nav"><span>About</span><span>Portfolio</span><span>Contact Us</span><span>Our Services</span><span>Blog</span></nav>
</header>

<section class="hero">
  <div class="abs hero-band" role="img" aria-label="Decorative flowing line pattern"></div>
  <h1 class="abs display" style="left:0;width:1200px;top:188px;text-align:center;font-size:46px;line-height:47px">Being online: a large<br>opportunity for your<br>practice</h1>
  <a class="abs link" style="left:520px;top:390px">Start a project <svg viewBox="0 0 36 36" fill="none" stroke="var(--blue)" stroke-width="2"><circle cx="18" cy="18" r="16"/><path d="M10 18h15M19 12l6 6-6 6"/></svg></a>
  <div class="abs social" style="left:132px;top:519px"><span></span><span></span><span></span></div>
  <svg class="abs" style="left:1005px;top:468px" width="30" height="68" viewBox="0 0 30 68" fill="none" stroke="var(--ink)" stroke-width="2"><path d="M15 0v64M3 52l12 12 12-12"/></svg>
</section>

<section class="grow">
  <h2 class="abs display" style="left:0;width:1200px;top:790px;text-align:center;font-size:33px;line-height:50px">Don't miss a new opportunity to grow<br>you practice with your online<br>presence.</h2>
  <div class="abs stats">
    <div class="stat" style="left:76px;top:26px"><div class="gem"><b>80%</b></div><p>Of internet users search for<br>health information</p></div>
    <div class="stat" style="left:416px;top:26px"><div class="gem"><b>50%</b></div><p>Would like information about a<br>specific health professional</p></div>
    <div class="stat" style="left:76px;top:140px"><div class="gem"><b>42%</b></div><p>Of individuals look at health<br>related consumer reviews</p></div>
    <div class="stat" style="left:416px;top:124px"><div class="gem"><b>41%</b></div><p>Of consumers say online<br>presence may impact their<br>choice of health professional</p></div>
  </div>
</section>

<section class="helping">
  <h2 class="abs display" style="left:136px;top:1354px;font-size:34px;line-height:38px">Meridian Reach : helping<br>those who help others</h2>
  <p class="abs" style="left:136px;top:1476px;width:410px;font-size:16px;line-height:26.6px;color:var(--muted)">You became a health professional because you wanted to make a difference and you obviously care about patient outcomes. At first things were great and you had plenty of patients but in the last few years there's more competition offering the same types of services and products that you do. We help you build your online assets through :</p>
  <a class="abs link" style="left:136px;top:1716px">Start a project <svg viewBox="0 0 36 36" fill="none" stroke="var(--blue)" stroke-width="2"><circle cx="18" cy="18" r="16"/><path d="M10 18h15M19 12l6 6-6 6"/></svg></a>

  <div class="service" style="left:592px;top:1478px">
    <svg viewBox="0 0 140 140" fill="none" stroke="var(--ink)" stroke-width="1.3"><path d="M70 4L136 70 70 136 4 70Z"/><g fill="var(--ink)"><circle cx="70" cy="4" r="3"/><circle cx="136" cy="70" r="3"/><circle cx="70" cy="136" r="3"/><circle cx="4" cy="70" r="3"/></g><circle cx="70" cy="70" r="34" fill="#fff"/><circle cx="70" cy="70" r="15"/><ellipse cx="70" cy="70" rx="7" ry="15"/><path d="M55 70h30M58 62h24M58 78h24"/></svg>
    Website<br>development</div>
  <div class="service" style="left:762px;top:1478px">
    <svg viewBox="0 0 140 140" fill="none" stroke="var(--ink)" stroke-width="1.3"><path d="M70 4L136 70 70 136 4 70Z"/><g fill="var(--ink)"><circle cx="70" cy="4" r="3"/><circle cx="136" cy="70" r="3"/><circle cx="70" cy="136" r="3"/><circle cx="4" cy="70" r="3"/></g><circle cx="70" cy="70" r="34" fill="#fff"/><path d="M68 64l16 6-7 2-2 7Z"/><path d="M62 56v5M54 64h5M57 58l3 3"/></svg>
    Social media<br>marketing</div>
  <div class="service" style="left:938px;top:1478px">
    <svg viewBox="0 0 140 140" fill="none" stroke="var(--ink)" stroke-width="1.3"><path d="M70 4L136 70 70 136 4 70Z"/><g fill="var(--ink)"><circle cx="70" cy="4" r="3"/><circle cx="136" cy="70" r="3"/><circle cx="70" cy="136" r="3"/><circle cx="4" cy="70" r="3"/></g><circle cx="70" cy="70" r="34" fill="#fff"/><circle cx="68" cy="72" r="13"/><circle cx="68" cy="72" r="7"/><circle cx="68" cy="72" r="1.5"/><path d="M68 72l14-14M78 58h4v-4"/></svg>
    Online Traffic<br>Strategies</div>
</section>

<section class="since">
  <h2 class="abs display" style="left:0;width:1200px;top:1876px;text-align:center;font-size:41px;font-weight:500">Helping clients since 2015</h2>
  <p class="abs" style="left:290px;top:1958px;width:620px;text-align:center;font-size:16px;line-height:26.6px">Meridian Reach specialises in helping health professionals &nbsp;like you, stand out from the busy crowd, find new patient and helps you be seen as the go-to person within your industry. Unlike most health professionals who solely rely on word of mouth, we use the latest online marketing techniques to grow you and your practice.</p>
  <div class="card" style="left:136px;top:2222px"><b>25%</b><span>Ecommerce<br>projects</span></div>
  <div class="card" style="left:314px;top:2158px"><b>63%</b><span>Healthcare and<br>medical</span></div>
  <div class="card" style="left:493px;top:2222px"><b>12%</b><span>Other pro<br>services</span></div>
  <p class="abs" style="left:730px;top:2188px;width:335px;font-size:16px;line-height:26.6px">While our niche has always been in the healthcare industry, Meridian Reach also has experience in providing solutions our e-commerce partners as well as other professional industries.</p>
  <a class="abs link" style="left:736px;top:2356px">Start a project <svg viewBox="0 0 36 36" fill="none" stroke="var(--blue)" stroke-width="2"><circle cx="18" cy="18" r="16"/><path d="M10 18h15M19 12l6 6-6 6"/></svg></a>
</section>

<section class="testimonials">
  <h2 class="abs display" style="left:0;width:1224px;top:2612px;text-align:center;font-size:35px;font-weight:500">See what our clients say</h2>
  <div class="avatar" style="left:183px;top:2603px;width:80px;height:80px" role="img" aria-label="Client portrait"><i></i></div>
  <div class="avatar" style="left:147px;top:2762px;width:64px;height:64px" role="img" aria-label="Client portrait"><i></i></div>
  <div class="avatar" style="left:198px;top:2900px;width:54px;height:54px" role="img" aria-label="Client portrait"><i></i></div>
  <div class="avatar" style="left:966px;top:2617px;width:60px;height:60px" role="img" aria-label="Client portrait"><i></i></div>
  <div class="avatar" style="left:988px;top:2763px;width:64px;height:64px" role="img" aria-label="Client portrait"><i></i></div>
  <div class="avatar" style="left:932px;top:2912px;width:64px;height:64px" role="img" aria-label="Client portrait"><i></i></div>
  <div class="abs" style="left:427px;top:2960px;width:388px;height:58px;background:#3a3b4e;border-radius:4px"></div>
  <div class="abs" style="left:399px;top:2950px;width:444px;height:42px;background:#33344a;border-radius:4px"></div>
  <div class="abs quote">Lorem ipsum dolor sit amet, consectetur adipiscing elit, sed do eiusmod tempor incididunt ut labore et dolore magna aliqua. Ut enim ad minim veniam.<br>Duis aute irure dolor in reprehenderit in voluptate velit esse cillum dolore eu fugiat nulla pariatur.<div class="who">DANA WHITFIELD</div></div>
  <div class="abs" style="left:557px;top:3066px;display:flex;gap:10px"><span style="width:30px;height:3px;background:var(--ink)"></span><span style="width:30px;height:3px;background:#c4c5cf"></span><span style="width:30px;height:3px;background:#c4c5cf"></span></div>
</section>

<section class="faq-section">
  <h2 class="abs display" style="left:0;width:1200px;top:3166px;text-align:center;font-size:41px;font-weight:500">Faq</h2>
  <div class="abs faq" style="top:3284px">
    <div class="faq-q"><span>Question 1 ?</span><svg width="18" height="12" viewBox="0 0 18 12" fill="none" stroke="var(--ink)" stroke-width="1.5"><path d="M2 3l7 7 7-7"/></svg></div>
    <div class="faq-q"><span>Question 2 ?</span><svg width="18" height="12" viewBox="0 0 18 12" fill="none" stroke="var(--ink)" stroke-width="1.5"><path d="M2 3l7 7 7-7"/></svg></div>
    <div class="faq-q open"><div><span>Question 3 ?</span><p class="faq-a">Lorem ipsum dolor sit amet, consectetur adipiscing elit, sed do eiusmod tempor incididunt ut labore et dolore magna aliqua. Ut enim ad minim veniam, quis nostrud exercitation</p></div><svg width="18" height="12" viewBox="0 0 18 12" fill="none" stroke="var(--ink)" stroke-width="1.5"><path d="M2 10l7-7 7 7"/></svg></div>
  </div>
</section>

<section class="blog">
  <h2 class="abs display" style="left:0;width:1200px;top:3794px;text-align:center;font-size:39px;font-weight:500">Blog</h2>
  <article class="post" style="left:132px"><div class="photo" role="img" aria-label="Woman smiling at her phone in a car" style="background:linear-gradient(135deg,#8a8680,#d8d2cc 55%,#6f7d8e)"></div><p class="meta"><em>SALES</em> - 3 MIN READ</p><h3>How to download UI Kit</h3><span class="more">Read more</span></article>
  <article class="post" style="left:453px"><div class="photo" role="img" aria-label="Man sitting on a sofa talking on the phone" style="background:linear-gradient(135deg,#ece8e2,#d6d2cc 55%,#8e8a80)"></div><p class="meta"><em>SALES</em> - 3 MIN READ</p><h3>How to download UI Kit</h3><span class="more">Read more</span></article>
  <article class="post" style="left:773px"><div class="photo" role="img" aria-label="Street vendor preparing food" style="background:linear-gradient(135deg,#3a4a6a,#7a5a4a 50%,#b24a36)"></div><p class="meta"><em>SALES</em> - 3 MIN READ</p><h3>How to download UI Kit</h3><span class="more">Read more</span></article>
</section>

<footer class="abs footer">
  <div class="abs brand" style="left:132px;top:90px;color:#fff"><span class="brand-dot"></span>meridian reach</div>
  <div class="abs" style="left:393px;top:78px"><h4>Pages</h4><ul><li>About</li><li>Portfolio</li><li>Our Services</li><li>Contact us</li><li>Blog</li></ul></div>
  <div class="abs" style="left:546px;top:78px"><h4>Other</h4><ul><li>Privacy Policy</li><li>Terms and conditions</li></ul><ul style="margin-top:16px"><li>Our Email :</li><li style="color:var(--blue)">hello@meridianreach.com.au</li></ul></div>
  <div class="abs" style="left:820px;top:78px"><h4>Sign up to our mailing list</h4><div class="input">Enter email adress</div><div class="send">Send</div></div>
  <p class="abs" style="left:132px;top:344px;font-size:10px;color:#c5c6d2">© 2022 Meridian Reach, All Right reserved</p>
  <div class="abs social foot-social" style="left:957px;top:338px;gap:14px"><span></span><span></span><span></span></div>
</footer>

</body>
</html>
```